Thai Restaurant Billboard Design

Design a billboard promoting food delivery during this Coronavirus time. We want to grab attention by embracing the Coronavirus and offering food delivery. People are sitting at home and this is the right time to promote food delivery.

I have the logo and spec sheet attached.

Target Market(s)

Anyone.

Requirements
Must have
• Top Heading should be big and bold:

Coronavirus Got You Quarantined?

Then put under

We Deliver
Healthy Thai Food!
Put the logo that is attached
408-231-7464
Nice to have
• Eyecatching. Creative.
Should not have
• Don't have any not haves. Make it look good.

```html
<!DOCTYPE html>
<html lang="en">
<head>
<meta charset="utf-8">
<title>Siam Lotus Kitchen – Delivery Billboard</title>
<link href="https://fonts.googleapis.com/css2?family=Montserrat:wght@400;500;700;800&display=swap" rel="stylesheet">
<style>
  :root {
    --stage: #dfe8f1;
    --board: #000000;
    --white: #ffffff;
    --yellow: #ffd200;
    --ink: #1a1a1a;
    --plate-dark: #2a2622;
    --plate-mid: #8a6a3c;
    --plate-warm: #d9a24a;
  }
  * { margin: 0; padding: 0; box-sizing: border-box; }
  html, body { width: 1200px; height: 780px; overflow: hidden; }
  body {
    background: var(--stage);
    font-family: "Montserrat", Arial, sans-serif;
    position: relative;
  }
  .billboard {
    position: absolute;
    left: 20px; top: 190px;
    width: 1160px; height: 399px;
    background: var(--board);
    overflow: hidden;
  }
  .dish-photo {
    position: absolute;
    left: -5px; top: 25px;
    width: 378px; height: 378px;
    border-radius: 50%;
    background: radial-gradient(circle at 45% 40%, var(--plate-warm) 0%, var(--plate-mid) 45%, var(--plate-dark) 72%, #111 100%);
  }
  .headline-top {
    position: absolute;
    left: 338px; top: 40px;
    color: var(--white);
    font-weight: 800;
    font-size: 90px;
    line-height: 1;
    letter-spacing: -1px;
  }
  .headline-sub {
    position: absolute;
    left: 417px; top: 136px;
    color: var(--white);
    font-weight: 800;
    font-size: 42px;
    line-height: 1;
  }
  .headline-accent {
    position: absolute;
    left: 614px; top: 121px;
    color: var(--yellow);
    font-weight: 800;
    font-size: 72px;
    line-height: 1;
  }
  .sparks { position: absolute; }
  .sparks-top { left: 912px; top: 30px; }
  .sparks-left { left: 352px; top: 158px; }
  .delivery-bar {
    position: absolute;
    left: 510px; top: 223px;
    width: 605px; height: 73px;
    background: var(--white);
    display: flex; align-items: center;
    padding-left: 22px;
    font-size: 33px;
    color: var(--ink);
    white-space: nowrap;
  }
  .delivery-bar .light { font-weight: 500; margin-right: 16px; }
  .delivery-bar .bold { font-weight: 800; }
  .delivery-badge {
    position: absolute;
    left: 412px; top: 206px;
    width: 106px; height: 106px;
    border-radius: 50%;
    background: var(--yellow);
    border: 3px solid var(--white);
    display: flex; align-items: center; justify-content: center;
  }
  .phone {
    position: absolute;
    left: 584px; top: 309px;
    display: flex; align-items: center; gap: 8px;
    color: var(--white);
    font-weight: 500;
    font-size: 62px;
    letter-spacing: 3px;
    line-height: 1;
  }
  .brand {
    position: absolute;
    left: 968px; top: 24px;
    width: 160px;
    text-align: center;
    color: var(--white);
    font-weight: 700;
    font-size: 14px;
    line-height: 1.2;
    white-space: nowrap;
  }
  .brand-mark {
    display: block;
    width: 34px; height: 34px;
    margin: 0 auto 14px;
    background: var(--white);
  }
</style>
</head>
<body>
  <main class="billboard">
    <div class="dish-photo" role="img" aria-label="Plate of Thai food with fried egg, crispy patty, fresh salad and salmon"></div>

    <h1 class="headline-top">Coronavirus</h1>
    <svg class="sparks sparks-top" width="52" height="48" viewBox="0 0 52 48" aria-hidden="true">
      <g stroke="var(--yellow)" stroke-width="3" stroke-linecap="round">
        <line x1="8" y1="30" x2="26" y2="6"/>
        <line x1="12" y1="38" x2="36" y2="28"/>
        <line x1="14" y1="44" x2="50" y2="45"/>
      </g>
    </svg>
    <p class="headline-sub">Got You</p>
    <svg class="sparks sparks-left" width="56" height="60" viewBox="0 0 56 60" aria-hidden="true">
      <g stroke="var(--yellow)" stroke-width="3" stroke-linecap="round">
        <line x1="2" y1="4" x2="46" y2="2"/>
        <line x1="10" y1="24" x2="46" y2="10"/>
        <line x1="20" y1="56" x2="50" y2="16"/>
      </g>
    </svg>
    <p class="headline-accent">Quarantined?</p>

    <div class="delivery-bar">
      <span class="light">We Deliver</span><span class="bold">Healthy Thai Food!</span>
    </div>
    <div class="delivery-badge">
      <svg width="62" height="50" viewBox="0 0 62 50" aria-hidden="true">
        <g fill="var(--ink)">
          <rect x="2" y="14" width="18" height="14" rx="2"/>
          <path d="M20 30 L40 30 L44 18 L50 18 L56 34 L14 34 Z"/>
          <rect x="44" y="10" width="8" height="4" rx="2"/>
          <circle cx="14" cy="40" r="7"/>
          <circle cx="50" cy="40" r="7"/>
        </g>
        <circle cx="14" cy="40" r="3" fill="var(--yellow)"/>
        <circle cx="50" cy="40" r="3" fill="var(--yellow)"/>
      </svg>
    </div>

    <div class="phone">
      <svg width="46" height="46" viewBox="0 0 48 48" aria-hidden="true">
        <path d="M10 6 L18 6 L21 16 L16 20 C19 27 22 30 28 33 L32 28 L42 31 L42 39 C42 42 40 44 37 44 C20 43 6 29 5 11 C5 8 7 6 10 6 Z" fill="var(--yellow)"/>
        <g fill="none" stroke="var(--yellow)" stroke-width="3" stroke-linecap="round">
          <path d="M28 6 A14 14 0 0 1 42 20"/>
          <path d="M27 13 A8 8 0 0 1 35 21"/>
        </g>
      </svg>
      <span class="phone-number">408-231-7464</span>
    </div>

    <div class="brand">
      <span class="brand-mark"></span>
      Siam Lotus Kitchen
    </div>
  </main>
</body>
</html>
```